2in1 Bartender & Sommelier needs a business card

I need a business card. I worked as a bartender in many places but I just finished a sommelier school and I would like a new business card. I like minimal design, natural materials and something what makes the people think :) I try to be creative in cocktail making, like little mixology, little twist on recipes... I like to travel and discover new places, cultures and of course interesting drinks and improve continously...live a little bit crazy life. And I like what I do...

Target Market(s)

restaurant/winebar managers, winemakers, other sommeliers and bartenders, people who work in food and beverage sector

Industry/Entity Type

Hospitality

Contact Information for Business Card

Rozsa Tarkany
Bartender & Sommelier
Phone: (FR) +33 6 4827 3190
(HU) +36 70 918 6352

Font styles to use
Script

Requirements
Must have
• Some sign, I am a bartender and sommelier as well.
Nice to have
• black and white maybe with 1 or 2 extra color
Should not have
• very colourful, to many things on the card

```html
<!DOCTYPE html>
<html lang="en">
<head>
<meta charset="utf-8">
<title>Rozsa Tarkany — Bartender &amp; Sommelier</title>
<link rel="stylesheet" href="https://fonts.googleapis.com/css2?family=Italianno&family=PT+Sans&display=swap">
<style>
  :root {
    --card: #747b91;
    --card-shade: #6d7489;
    --line-dark: #4f5569;
    --line-light: #b4b9c9;
    --ink: #1d2030;
    --icon: #15171f;
  }
  html, body {
    margin: 0;
    width: 1200px;
    height: 675px;
    overflow: hidden;
    background: var(--card);
  }
  .card {
    position: relative;
    width: 1200px;
    height: 675px;
    background: linear-gradient(100deg, var(--card-shade) 0%, var(--card) 40%, var(--card) 100%);
    overflow: hidden;
  }
  .card__lines {
    position: absolute;
    inset: 0;
  }
  .contact {
    position: absolute;
    left: 720px;
    top: 40px;
    color: var(--ink);
    font-family: "PT Sans", sans-serif;
    font-size: 27px;
    line-height: 1.22;
  }
  .contact__icon {
    display: block;
    width: 62px;
    height: 62px;
    margin: 0 0 18px 70px;
  }
  .contact__line { margin: 0; white-space: nowrap; }
  .identity {
    position: absolute;
    left: 430px;
    top: 250px;
    color: var(--ink);
  }
  .identity__mark {
    display: block;
    width: 92px;
    height: 92px;
    margin-left: 40px;
  }
  .identity__name {
    margin: 0;
    font-family: "Italianno", cursive;
    font-weight: 400;
    font-size: 104px;
    line-height: 0.95;
    letter-spacing: 1px;
  }
  .identity__role {
    margin: 0 0 0 34px;
    font-family: "Italianno", cursive;
    font-size: 44px;
    line-height: 1;
  }
</style>
</head>
<body>
  <main class="card">
    <svg class="card__lines" width="1200" height="675" viewBox="0 0 1200 675" aria-hidden="true">
      <defs>
        <linearGradient id="fade-left" x1="0" y1="0" x2="1" y2="0">
          <stop offset="0" stop-color="#fff" stop-opacity="0"/>
          <stop offset="0.6" stop-color="#fff" stop-opacity="1"/>
        </linearGradient>
        <mask id="fade-mask">
          <rect x="820" y="250" width="380" height="180" fill="url(#fade-left)"/>
        </mask>
      </defs>
      <g class="stripes-left" stroke-width="2">
        <line x1="30" y1="0" x2="18" y2="675" stroke="var(--line-dark)"/>
        <line x1="78" y1="0" x2="68" y2="675" stroke="var(--line-light)"/>
        <line x1="92" y1="0" x2="82" y2="675" stroke="var(--line-dark)"/>
        <line x1="140" y1="0" x2="130" y2="675" stroke="var(--line-light)"/>
        <line x1="158" y1="0" x2="148" y2="675" stroke="var(--line-dark)"/>
        <line x1="196" y1="0" x2="188" y2="675" stroke="var(--line-light)"/>
        <line x1="218" y1="0" x2="210" y2="675" stroke="var(--line-dark)"/>
        <line x1="300" y1="0" x2="294" y2="675" stroke="var(--line-dark)"/>
      </g>
      <g class="stripes-right" stroke-width="2" mask="url(#fade-mask)">
        <line x1="830" y1="282" x2="1200" y2="268" stroke="var(--line-dark)"/>
        <line x1="830" y1="312" x2="1200" y2="296" stroke="var(--line-light)"/>
        <line x1="830" y1="328" x2="1200" y2="314" stroke="var(--line-dark)"/>
        <line x1="830" y1="356" x2="1200" y2="342" stroke="var(--line-light)"/>
        <line x1="830" y1="374" x2="1200" y2="360" stroke="var(--line-dark)"/>
        <line x1="830" y1="404" x2="1200" y2="390" stroke="var(--line-light)"/>
      </g>
    </svg>

    <section class="contact">
      <svg class="contact__icon" viewBox="0 0 62 62" role="img" aria-label="Phone">
        <circle cx="31" cy="31" r="30" fill="var(--icon)"/>
        <path d="M14 26c0-6 34-6 34 0v3h-8v-3c-5-2-13-2-18 0v3h-8z" fill="var(--card)"/>
        <path d="M21 30h20l5 14H16z" fill="var(--card)"/>
        <circle cx="31" cy="37" r="4.5" fill="var(--icon)"/>
        <circle cx="31" cy="37" r="1.8" fill="var(--card)"/>
      </svg>
      <p class="contact__line">(FR) +33 6 4827 3190</p>
      <p class="contact__line">&nbsp;(HU)+36 70 918 6352</p>
    </section>

    <section class="identity">
      <svg class="identity__mark" viewBox="0 0 92 92" aria-hidden="true">
        <circle cx="46" cy="46" r="44" fill="var(--card-shade)" stroke="var(--line-dark)" stroke-width="2"/>
        <circle cx="46" cy="46" r="34" fill="var(--icon)"/>
      </svg>
      <h1 class="identity__name">Rozsa Tarkany</h1>
      <p class="identity__role">Bartender &amp; Sommelier</p>
    </section>
  </main>
</body>
</html>
```